Figure for a research paper

I am working on designing a figure for a research paper that illustrates the effect of KORA Pathway assessment on student outcomes over time by impacting teacher bias and teacher perception of student growth. I built the attached figure via powerpoint. It includes the very basic elements but it does not look great and I am not sure that it is clearly depicting what I am hoping to illustrate. I would like for you to build an illustration of this idea that i can include in the paper.

```html
<!DOCTYPE html>
<html lang="en">
<head>
<meta charset="utf-8">
<title>KORA Pathway Assessment and SEL Program Effectiveness</title>
<link rel="stylesheet" href="https://fonts.googleapis.com/css2?family=Poppins:wght@500;600&display=swap">
<style>
  :root {
    --bg-top: #fbfbfb;
    --bg-bottom: #ececec;
    --ink: #2e2a2b;
    --grid: #d6d6d6;
    --bias: #fc84fc;
    --bias-light: #fdbafd;
    --perception: #f65a33;
    --perception-light: #f8a58c;
    --assessment: #b4dc1c;
    --trend: #0a4db8;
    --trend-light: #6aaef5;
    --trend-dark: #0a2f7a;
  }
  html, body {
    margin: 0;
    width: 1200px;
    height: 719px;
    overflow: hidden;
  }
  body {
    background: linear-gradient(180deg, var(--bg-top) 0%, var(--bg-bottom) 100%);
    font-family: "Poppins", sans-serif;
  }
  .figure { display: block; width: 1200px; height: 719px; }
  .axis-label { font-weight: 600; font-size: 15.5px; fill: var(--ink); }
  .region-label { font-weight: 600; fill: var(--ink); }
  .region-label--bias { font-size: 15px; }
  .region-label--perception { font-size: 11px; }
  .region-label--assessment { font-size: 12.5px; }
  .grid-line { stroke: var(--grid); stroke-width: 1; stroke-dasharray: 1.5 3; }
  .axis { stroke: var(--ink); stroke-width: 2.2; stroke-linecap: round; }
  .tick { fill: var(--ink); }
  .effect-arrow { fill: var(--ink); }
</style>
</head>
<body>
<svg class="figure" viewBox="0 0 1200 719" xmlns="http://www.w3.org/2000/svg" aria-labelledby="fig-title">
  <title id="fig-title">Effectiveness of SEL program on the student over time, with KORA Pathway framework assessment reducing teacher bias and inaccurate perception of growth</title>
  <defs>
    <linearGradient id="bias-fill" x1="0" y1="0" x2="0" y2="1">
      <stop offset="0" stop-color="var(--bias)"/>
      <stop offset="0.18" stop-color="var(--bias-light)"/>
      <stop offset="0.45" stop-color="var(--bias)"/>
      <stop offset="1" stop-color="var(--bias)"/>
    </linearGradient>
    <linearGradient id="perception-fill" x1="0" y1="0" x2="0" y2="1">
      <stop offset="0" stop-color="var(--perception)"/>
      <stop offset="0.13" stop-color="var(--perception-light)"/>
      <stop offset="0.33" stop-color="var(--perception)"/>
      <stop offset="1" stop-color="var(--perception)"/>
    </linearGradient>
    <linearGradient id="trend-stroke" x1="291" y1="531" x2="985" y2="302" gradientUnits="userSpaceOnUse">
      <stop offset="0" stop-color="var(--trend)"/>
      <stop offset="0.2" stop-color="var(--trend)"/>
      <stop offset="0.32" stop-color="var(--trend-light)"/>
      <stop offset="0.45" stop-color="var(--trend-dark)"/>
      <stop offset="0.62" stop-color="var(--trend)"/>
      <stop offset="0.72" stop-color="var(--trend-light)"/>
      <stop offset="0.82" stop-color="var(--trend)"/>
      <stop offset="1" stop-color="var(--trend)"/>
    </linearGradient>
    <linearGradient id="arrow-down" x1="0" y1="0" x2="0" y2="1">
      <stop offset="0" stop-color="var(--ink)" stop-opacity="0"/>
      <stop offset="0.5" stop-color="var(--ink)"/>
    </linearGradient>
    <linearGradient id="arrow-up" x1="0" y1="1" x2="0" y2="0">
      <stop offset="0" stop-color="var(--ink)" stop-opacity="0"/>
      <stop offset="0.5" stop-color="var(--ink)"/>
    </linearGradient>
    <radialGradient id="axis-shadow" cx="0.5" cy="0.5" r="0.5">
      <stop offset="0" stop-color="#000" stop-opacity="0.12"/>
      <stop offset="1" stop-color="#000" stop-opacity="0"/>
    </radialGradient>
  </defs>

  <!-- grid -->
  <g class="grid">
    <line class="grid-line" x1="291" y1="187" x2="979" y2="187"/>
    <line class="grid-line" x1="291" y1="221" x2="979" y2="221"/>
    <line class="grid-line" x1="291" y1="256" x2="979" y2="256"/>
    <line class="grid-line" x1="291" y1="290" x2="979" y2="290"/>
    <line class="grid-line" x1="291" y1="324" x2="979" y2="324"/>
    <line class="grid-line" x1="291" y1="359" x2="979" y2="359"/>
    <line class="grid-line" x1="291" y1="393" x2="979" y2="393"/>
    <line class="grid-line" x1="325" y1="187" x2="325" y2="417"/>
    <line class="grid-line" x1="360" y1="187" x2="360" y2="417"/>
    <line class="grid-line" x1="394" y1="187" x2="394" y2="417"/>
    <line class="grid-line" x1="428" y1="187" x2="428" y2="417"/>
    <line class="grid-line" x1="463" y1="187" x2="463" y2="417"/>
    <line class="grid-line" x1="497" y1="187" x2="497" y2="417"/>
    <line class="grid-line" x1="531" y1="187" x2="531" y2="417"/>
    <line class="grid-line" x1="566" y1="187" x2="566" y2="417"/>
    <line class="grid-line" x1="600" y1="187" x2="600" y2="417"/>
    <line class="grid-line" x1="635" y1="187" x2="635" y2="304"/>
    <line class="grid-line" x1="669" y1="187" x2="669" y2="304"/>
    <line class="grid-line" x1="703" y1="187" x2="703" y2="304"/>
    <line class="grid-line" x1="738" y1="187" x2="738" y2="304"/>
    <line class="grid-line" x1="772" y1="187" x2="772" y2="304"/>
    <line class="grid-line" x1="807" y1="187" x2="807" y2="304"/>
    <line class="grid-line" x1="841" y1="187" x2="841" y2="304"/>
    <line class="grid-line" x1="876" y1="187" x2="876" y2="304"/>
    <line class="grid-line" x1="910" y1="187" x2="910" y2="304"/>
    <line class="grid-line" x1="944" y1="187" x2="944" y2="304"/>
    <line class="grid-line" x1="979" y1="187" x2="979" y2="304"/>
  </g>

  <!-- regions -->
  <rect class="region region--bias" x="291" y="417" width="344" height="114" fill="url(#bias-fill)"/>
  <rect class="region region--perception" x="635" y="304" width="344" height="120" fill="url(#perception-fill)"/>
  <polygon class="region region--assessment" points="291,531 979,304 979,531" fill="var(--assessment)"/>

  <!-- trend line -->
  <line x1="293" y1="530" x2="978" y2="305" stroke="url(#trend-stroke)" stroke-width="3.2"/>
  <polygon points="988,300 972,300.5 978,310.5" fill="var(--trend)"/>

  <!-- axes -->
  <ellipse cx="635" cy="536" rx="390" ry="8" fill="url(#axis-shadow)"/>
  <line class="axis" x1="291" y1="187" x2="291" y2="531"/>
  <line class="axis" x1="291" y1="531" x2="979" y2="531"/>
  <g class="ticks">
    <circle class="tick" cx="291" cy="187" r="2.2"/>
    <circle class="tick" cx="291" cy="209" r="2.2"/>
    <circle class="tick" cx="291" cy="231" r="2.2"/>
    <circle class="tick" cx="291" cy="253" r="2.2"/>
    <circle class="tick" cx="291" cy="275" r="2.2"/>
    <circle class="tick" cx="291" cy="297" r="2.2"/>
    <circle class="tick" cx="291" cy="319" r="2.2"/>
    <circle class="tick" cx="291" cy="341" r="2.2"/>
    <circle class="tick" cx="291" cy="363" r="2.2"/>
    <circle class="tick" cx="291" cy="385" r="2.2"/>
    <circle class="tick" cx="291" cy="407" r="2.2"/>
    <circle class="tick" cx="291" cy="429" r="2.2"/>
    <circle class="tick" cx="291" cy="451" r="2.2"/>
    <circle class="tick" cx="291" cy="473" r="2.2"/>
    <circle class="tick" cx="291" cy="495" r="2.2"/>
    <circle class="tick" cx="291" cy="517" r="2.2"/>
    <circle class="tick" cx="307" cy="531" r="2.2"/>
    <circle class="tick" cx="329" cy="531" r="2.2"/>
    <circle class="tick" cx="351" cy="531" r="2.2"/>
    <circle class="tick" cx="372" cy="531" r="2.2"/>
    <circle class="tick" cx="394" cy="531" r="2.2"/>
    <circle class="tick" cx="416" cy="531" r="2.2"/>
    <circle class="tick" cx="437" cy="531" r="2.2"/>
    <circle class="tick" cx="459" cy="531" r="2.2"/>
    <circle class="tick" cx="481" cy="531" r="2.2"/>
    <circle class="tick" cx="502" cy="531" r="2.2"/>
    <circle class="tick" cx="524" cy="531" r="2.2"/>
    <circle class="tick" cx="546" cy="531" r="2.2"/>
    <circle class="tick" cx="567" cy="531" r="2.2"/>
    <circle class="tick" cx="589" cy="531" r="2.2"/>
    <circle class="tick" cx="611" cy="531" r="2.2"/>
    <circle class="tick" cx="632" cy="531" r="2.2"/>
    <circle class="tick" cx="654" cy="531" r="2.2"/>
    <circle class="tick" cx="676" cy="531" r="2.2"/>
    <circle class="tick" cx="697" cy="531" r="2.2"/>
    <circle class="tick" cx="719" cy="531" r="2.2"/>
    <circle class="tick" cx="741" cy="531" r="2.2"/>
    <circle class="tick" cx="762" cy="531" r="2.2"/>
    <circle class="tick" cx="784" cy="531" r="2.2"/>
    <circle class="tick" cx="806" cy="531" r="2.2"/>
    <circle class="tick" cx="827" cy="531" r="2.2"/>
    <circle class="tick" cx="849" cy="531" r="2.2"/>
    <circle class="tick" cx="871" cy="531" r="2.2"/>
    <circle class="tick" cx="892" cy="531" r="2.2"/>
    <circle class="tick" cx="914" cy="531" r="2.2"/>
    <circle class="tick" cx="936" cy="531" r="2.2"/>
    <circle class="tick" cx="957" cy="531" r="2.2"/>
    <circle class="tick" cx="979" cy="531" r="2.2"/>
  </g>

  <!-- effect arrows -->
  <g class="effect-arrow">
    <rect x="363.5" y="459" width="5" height="14" fill="url(#arrow-down)"/>
    <polygon points="358.5,472 373.5,472 366,485"/>
    <rect x="690.5" y="354" width="5" height="14" fill="url(#arrow-down)"/>
    <polygon points="685.5,367 700.5,367 693,381"/>
    <rect x="799.5" y="430" width="5" height="14" fill="url(#arrow-up)"/>
    <polygon points="794.5,431 809.5,431 802,417"/>
  </g>

  <!-- labels -->
  <g class="axis-label" text-anchor="end">
    <text x="252" y="308">Effectiveness</text>
    <text x="252" y="335">of SEL</text>
    <text x="252" y="362">Program</text>
    <text x="252" y="390">on the</text>
    <text x="252" y="417">Student</text>
  </g>
  <text class="axis-label" x="627" y="560" text-anchor="middle">Time</text>

  <text class="region-label region-label--bias" x="317" y="448">Teacher Bias</text>
  <text class="region-label region-label--perception" x="656" y="331">Teacher’s inaccurate perception</text>
  <text class="region-label region-label--perception" x="661" y="343">of student growth (or learning)</text>
  <text class="region-label region-label--assessment" x="802" y="474" text-anchor="middle">KORA Pathway Framework Assessment</text>
</svg>
</body>
</html>
```